IT Consulting Business needs a web design

We need a web design for an IT Consulting company called "Verunex". We want to replace the existing web site (www.verunex-example.com) with a new design. Our services are IT Consulting, IT Training, IT Outsourcing.
We would like to see designs that communicate "Trusted IT Advisor" with modern & bold design.

We would like to see the design of 2 pages:
1. Home page (www.verunex-example.com)
2. The detail page (http://www.verunex-example.com/index_files/consulting.htm)

```html
<!DOCTYPE html>
<html lang="en">
<head>
<meta charset="utf-8">
<title>Verunex – IT Consulting</title>
<link rel="stylesheet" href="https://fonts.googleapis.com/css2?family=PT+Sans:ital,wght@0,400;0,700;1,400&family=Arimo:wght@400;700&display=swap">
<style>
:root{
  --page-bg:#e9e9e9;
  --sheet:#ffffff;
  --band:#f3f3f3;
  --heading:#777777;
  --text:#6f6f6f;
  --body-dark:#444444;
  --brand-blue:#1459b0;
  --icon-blue:#2c5fb8;
  --rule:#d6d6d6;
  --nav:#a8a8a8;
  --social:#4f4f4f;
  --badge:#c9c9c9;
}
*{margin:0;padding:0;box-sizing:border-box}
html,body{width:1200px;height:900px;overflow:hidden}
body{background:var(--page-bg);font-family:"Arimo",Arial,sans-serif;position:relative}
.sheet{position:absolute;left:24px;top:0;width:1146px;height:900px;background:var(--sheet)}
.abs{position:absolute}

/* features row */
.feature{position:absolute;top:0;width:200px;margin-left:-100px;text-align:center}
.feature svg{display:block;margin:0 auto;height:30px}
.feature h3{font-family:"PT Sans",sans-serif;font-style:italic;font-weight:400;font-size:25px;color:var(--heading);margin-top:16px;line-height:30px}
.feature p{font-size:11.5px;color:var(--text);line-height:16px;margin-top:3px}

/* services band */
.band{position:absolute;left:24px;top:157px;width:1146px;height:473px;background:var(--band)}
.tagline{position:absolute;left:0;top:176px;width:1178px;text-align:center;font-family:"PT Sans",sans-serif;font-style:italic;font-size:25.5px;color:#6a6a6a}
.tagline em{color:var(--brand-blue);font-style:italic}
.card{position:absolute;top:227px;width:324px;height:358px;background:var(--sheet);box-shadow:0 18px 14px -12px rgba(0,0,0,.22)}
.card-photo{height:216px}
.photo-handshake{background:linear-gradient(120deg,#dfe9f6 0%,#9fbde4 45%,#4d82cc 100%)}
.photo-meeting{background:linear-gradient(160deg,#f4f4f4 0%,#c9cdd3 50%,#6f8cab 100%)}
.photo-map{background:linear-gradient(150deg,#c9d8f7 0%,#e3ebfb 55%,#b9ccf2 100%)}
.card-title{position:absolute;left:27px;top:234px;font-family:"PT Sans",sans-serif;font-style:italic;font-size:25px;color:var(--heading)}
.card-badge{position:absolute;right:37px;top:238px;width:27px;height:27px;border-radius:50%;background:var(--badge)}
.card-badge svg{width:27px;height:27px}
.card-rule{position:absolute;left:27px;right:25px;top:284px;height:3px;border-top:1px solid var(--rule);border-bottom:1px solid var(--rule)}
.card-text{position:absolute;left:27px;top:302px;width:280px;font-size:11.5px;line-height:15px;color:var(--text)}

/* lower section */
.section-title{font-family:"PT Sans",sans-serif;font-style:italic;font-size:21px;color:var(--brand-blue)}
.about-text{position:absolute;left:87px;top:712px;width:670px;font-size:12.4px;line-height:18px;color:var(--body-dark)}
.services-list{position:absolute;left:87px;top:754px;width:680px;font-size:12.4px;line-height:18px;color:var(--body-dark)}
.services-list strong{display:block;font-weight:700}
.services-list ul{list-style:none;display:grid;grid-template-columns:302px 1fr}
.services-list li::before{content:"· "}
.divider-v{position:absolute;left:787px;top:650px;height:156px;border-left:1px dotted #9a9a9a}
.social{position:absolute;top:721px;width:28px;height:28px;border-radius:50%;background:var(--social)}
.divider-h{position:absolute;left:86px;top:831px;width:1024px;border-top:1px solid #e2e2e2}
.site-nav{position:absolute;left:89px;top:859px;font-size:12.3px;color:var(--nav)}
.site-nav a{color:inherit;text-decoration:none;position:absolute;white-space:nowrap}
.brand{position:absolute;right:108px;top:852px;font-family:"PT Sans",sans-serif;font-weight:700;font-size:26px;color:var(--brand-blue)}
</style>
</head>
<body>
<div class="sheet"></div>

<section class="features">
  <div class="feature" style="left:153px">
    <svg viewBox="0 0 54 30" width="54"><path d="M2 8h12l16 14h10M2 22h12l6-5M26 13l4-5h10" fill="none" stroke="var(--icon-blue)" stroke-width="5"/><path d="M40 0l12 8-12 8zM40 14l12 8-12 8z" fill="var(--icon-blue)"/></svg>
    <h3>Fast</h3><p>Lorem ipsum dolor sit amet<br>consectetur adipiscing</p>
  </div>
  <div class="feature" style="left:369px">
    <svg viewBox="0 0 50 30" width="50"><path d="M3 2v25h40V16" fill="none" stroke="var(--icon-blue)" stroke-width="5"/><path d="M14 22c2-9 9-13 20-13V3l12 9-12 9v-6c-8 0-14 2-20 7z" fill="var(--icon-blue)"/></svg>
    <h3>High Quality</h3><p>Lorem ipsum dolor sit amet<br>consectetur adipiscing</p>
  </div>
  <div class="feature" style="left:599px">
    <svg viewBox="0 0 54 30" width="54"><path d="M6 2l40 26M46 2L6 28" stroke="var(--icon-blue)" stroke-width="7"/></svg>
    <h3>Services</h3><p>Lorem ipsum dolor sit amet<br>consectetur adipiscing</p>
  </div>
  <div class="feature" style="left:830px">
    <svg viewBox="0 0 48 30" width="48"><path d="M2 4h6v5H2zM2 13h6v5H2zM2 22h6v5H2zM13 4h33v5H13zM13 13h33v5H13zM13 22h33v5H13z" fill="var(--icon-blue)"/></svg>
    <h3>Customised</h3><p>Lorem ipsum dolor sit amet<br>consectetur adipiscing</p>
  </div>
  <div class="feature" style="left:1036px">
    <svg viewBox="0 0 50 30" width="50"><path d="M3 0v12M14 6h32v22H14z" fill="none" stroke="var(--icon-blue)" stroke-width="5"/></svg>
    <h3>Customer focus</h3><p>Lorem ipsum dolor sit amet<br>consectetur adipiscing</p>
  </div>
</section>

<section class="band"></section>
<h1 class="tagline">Experienced, certified professionals provide <em>IT consulting</em> by industry recommended practices.</h1>

<article class="card" style="left:85px">
  <div class="card-photo photo-handshake" role="img" aria-label="Businessman offering a handshake against a blue sky"></div>
  <h2 class="card-title">IT Consulting</h2>
  <div class="card-badge"><svg viewBox="0 0 27 27"><path d="M10 7l10 6.5L10 20z" fill="#fff"/></svg></div>
  <div class="card-rule"></div>
  <p class="card-text">Lorem ipsum dolor sit amet consec adipiscing elitvi vamus ut neque augtortor velit bibenn.</p>
</article>
<article class="card" style="left:434px">
  <div class="card-photo photo-meeting" role="img" aria-label="Colleagues in a meeting around a laptop"></div>
  <h2 class="card-title">IT Training</h2>
  <div class="card-badge"><svg viewBox="0 0 27 27"><circle cx="13.5" cy="10" r="3.5" fill="#fff"/><path d="M7 20c0-4 3-6 6.5-6s6.5 2 6.5 6z" fill="#fff"/></svg></div>
  <div class="card-rule"></div>
  <p class="card-text">Lorem ipsum dolor sit amet consec adipiscing elitvi vamus ut neque augtortor velit bibenn.</p>
</article>
<article class="card" style="left:784px">
  <div class="card-photo photo-map" role="img" aria-label="World map with silhouettes of a crowd of people"></div>
  <h2 class="card-title">IT Outsourcing</h2>
  <div class="card-badge"><svg viewBox="0 0 27 27"><g fill="none" stroke="#fff" stroke-width="1.4"><circle cx="13.5" cy="13.5" r="8"/><ellipse cx="13.5" cy="13.5" rx="3.5" ry="8"/><path d="M5.5 13.5h16M7 9h13M7 18h13"/></g></svg></div>
  <div class="card-rule"></div>
  <p class="card-text">Lorem ipsum dolor sit amet consec adipiscing elitvi vamus ut neque augtortor velit bibenn.</p>
</article>

<h2 class="section-title abs" style="left:91px;top:666px">About our Consulting Services</h2>
<p class="about-text">Our experienced, certified professionals provides IT consulting using industry recommended practices. We are specialized in Corvanta Business Productivity Platform using Corvanta ShareGrid Technologies and Business Intelligence Platform.</p>
<div class="services-list">
  <strong>Some of our services are:</strong>
  <ul>
    <li>Strategic technology consulting and advice</li>
    <li>Business technology improvements</li>
    <li>Business technology reviews, audits, and studies</li>
    <li>Solution architecture &amp; implementation for applications of all sizes</li>
  </ul>
</div>
<div class="divider-v"></div>
<h2 class="section-title abs" style="left:832px;top:666px">Stay Connected</h2>
<span class="social" style="left:832px" aria-label="Social link"></span>
<span class="social" style="left:872px" aria-label="Social link"></span>
<span class="social" style="left:912px" aria-label="Social link"></span>
<span class="social" style="left:951px" aria-label="Social link"></span>

<div class="divider-h"></div>
<nav class="site-nav">
  <a href="#" style="left:0">Home</a>
  <a href="#" style="left:88px">Services</a>
  <a href="#" style="left:180px">Our Expertise</a>
  <a href="#" style="left:306px">Jobs</a>
  <a href="#" style="left:383px">About Us</a>
  <a href="#" style="left:478px">Contact Us</a>
</nav>
<div class="brand">Verunex</div>
</body>
</html>
```